Cobalt MesaLighting and Design Web Page

We are a Sales Agency that represents 40+ LED Lighting manufacturers primarily in new commercial, industrial and architectural construction projects. We also are active in the Re-Light and Retrofit Lighting market.
Our current web page can be found at www.cobaltmesalighting.example. Our local competitors are www.brightfieldlampsnw.example,. We would like a more dynamic website that will list our manufacturers we represent and links to their websites. Please offer suggestions to provide a more dynamic website using our new logo which is attached. Please use the color scheme from logo. The final design should communicate innovation and expertise in LED lighting.

Target Market(s)

Architects, Lighting designers, Electrical Engineers, Electrical Contractors, Electrical Distributors, Facility Engineers, Energy Engineers

Industry/Entity Type

Construction

Number of Pages Required

5+ page

Font styles to use
Other font styles liked:
• MS Reference Sans Serif, or close to our LOGO font.

Colors
f78f20
959595

Requirements
Must have
• Logo incorporated with matching background, clean professional look based on logo, links to our manufacturers web page
Nice to have
• LED Lighting project stock photos as examples
Should not have
• crowded pages with text

```html
<!DOCTYPE html>
<html lang="en">
<head>
<meta charset="utf-8">
<title>Cobalt Mesa Lighting and Design</title>
<link href="https://fonts.googleapis.com/css2?family=Roboto:wght@400;500;700&family=Open+Sans:wght@400;600&display=swap" rel="stylesheet">
<style>
:root{
  --orange:#f47b20;
  --orange-deep:#e5661a;
  --grey:#959595;
  --ink:#222;
  --text:#555;
  --light:#f1f1f1;
  --panel:#e9e9e9;
  --dark:#0d0d0d;
}
*{margin:0;padding:0;box-sizing:border-box}
html,body{width:1200px;height:4700px;overflow:hidden}
body{font-family:"Open Sans",Arial,sans-serif;color:var(--text);background:#fff;position:relative}
.section{position:absolute;left:0;width:1200px}
h2.title{font-family:"Roboto",Arial,sans-serif;font-weight:500;font-size:30px;color:var(--ink);text-align:center;letter-spacing:1px;text-transform:uppercase}
.underline{width:60px;height:3px;background:var(--orange);margin:10px auto 0}
.btn{display:inline-block;background:var(--orange);color:#fff;font-family:"Roboto",Arial,sans-serif;font-size:14px;font-weight:500;text-transform:uppercase;padding:9px 20px;letter-spacing:.5px}
.photo{position:absolute}

/* header */
.header{top:0;height:125px;background:#fff}
.brand{position:absolute;left:70px;top:18px;display:flex;align-items:center;gap:14px}
.brand-dot{width:70px;height:70px;border-radius:50%;background:var(--orange);flex:none}
.brand-name{font-family:"Roboto",Arial,sans-serif;font-weight:700;font-size:24px;color:var(--grey);line-height:1.05;text-transform:uppercase;white-space:nowrap}
.phone-tab{position:absolute;right:0;top:0;width:330px;height:44px;background:var(--grey);color:#fff;font-family:"Roboto",Arial,sans-serif;font-size:22px;font-weight:500;display:flex;align-items:center;justify-content:center;gap:12px}
.nav{position:absolute;right:0;top:82px;width:880px;height:40px;background:var(--orange);display:flex;align-items:center;padding-left:20px}
.nav a{color:#fff;text-decoration:none;font-family:"Roboto",Arial,sans-serif;font-size:15px;text-transform:uppercase;padding:0 13px;height:40px;line-height:40px}
.nav a.active{background:var(--orange-deep)}

/* hero */
.hero{top:125px;height:540px;background:linear-gradient(160deg,#3e63a8 0%,#5a4b86 35%,#c35a2b 70%,#2a1c2e 100%)}
.hero-text{position:absolute;left:90px;top:140px;color:#fff;font-family:"Roboto",Arial,sans-serif;font-size:62px;line-height:1.1;text-transform:uppercase;font-weight:400}
.hero-text b{font-weight:700}

/* features */
.features{top:665px;height:370px;background:var(--light);display:flex;justify-content:center;gap:30px;padding-top:40px}
.feature{width:240px;text-align:center}
.feature-icon{width:92px;height:92px;border-radius:50%;background:var(--orange);margin:0 auto;border:8px solid #fff;box-shadow:0 0 0 1px #ddd;display:flex;align-items:center;justify-content:center}
.feature h3{font-family:"Roboto",Arial,sans-serif;font-size:20px;color:var(--ink);margin:55px 0 10px;font-weight:500}
.feature p{font-size:14px;line-height:1.6}

/* welcome */
.welcome{top:1070px;height:400px}
.welcome h2{margin-top:10px}
.welcome-photo{left:0;top:110px;width:580px;height:290px;background:linear-gradient(120deg,#b07a44,#e2c89c 50%,#8b5a2b)}
.welcome-copy{position:absolute;left:612px;top:120px;width:510px;font-size:14px;line-height:1.65}
.welcome-copy p{margin-bottom:14px}

/* services */
.services{top:1500px;height:420px}
.services-band{position:absolute;left:0;top:200px}
.service-row{position:absolute;left:70px;top:90px;display:flex;gap:27px}
.service{width:245px;color:#fff}
.service .thumb{width:245px;height:185px;position:relative}
.service h4{font-family:"Roboto",Arial,sans-serif;font-size:17px;font-weight:700;margin:14px 0 6px}
.service p{font-size:13px;line-height:1.5}
.training-label{position:absolute;left:0;right:0;top:120px;text-align:center;color:#ffcc00;font-family:"Roboto",Arial,sans-serif;font-weight:700;font-size:26px}

/* mission */
.mission{top:1940px;height:470px}
.mission-copy{position:absolute;left:150px;top:190px;width:900px;text-align:center;color:#fff}
.mission-copy h2{font-family:"Roboto",Arial,sans-serif;font-size:32px;font-weight:500;margin-bottom:12px}
.mission-copy p{font-size:15px;line-height:1.6}

/* projects */
.projects{top:2460px;height:440px}
.col-title{position:absolute;top:20px;font-family:"Roboto",Arial,sans-serif;font-size:26px;font-weight:500;color:var(--ink);text-transform:uppercase;border-bottom:2px solid #ccc;padding-bottom:10px}
.col-title span{display:block;width:60px;height:3px;background:var(--orange);position:absolute;bottom:-2px;left:0}
.project{position:absolute;top:100px;width:240px}
.project .thumb{width:240px;height:175px;background:linear-gradient(135deg,#5a2a12,#c98a3c 55%,#3d1c0e)}
.project h5{font-family:"Roboto",Arial,sans-serif;font-size:16px;color:var(--ink);font-weight:500;margin:18px 0 18px}
.project .btn{font-size:13px;padding:8px 16px}

/* line card */
.linecard{top:2930px;height:430px}
.brands{position:absolute;left:70px;top:90px;display:flex;gap:27px}
.brand-card{width:245px}
.brand-tile{height:155px;border:2px solid #ddd;display:flex;align-items:center;justify-content:center;font-family:"Roboto",Arial,sans-serif;font-size:26px;font-weight:700;color:#333;text-transform:uppercase}
.brand-card h5{font-family:"Roboto",Arial,sans-serif;font-size:15px;color:var(--ink);margin:16px 0 6px;font-weight:500}
.brand-card p{font-size:13px;line-height:1.5}
.linecard .btn{position:absolute;left:553px;top:385px;font-size:13px}

/* gallery */
.gallery{top:3410px;height:570px;background:var(--dark)}
.gallery h2{color:#fff;font-size:27px;padding-top:58px}
.gallery-grid{position:absolute;left:100px;top:130px;width:1000px;height:345px;display:grid;grid-template-columns:repeat(4,1fr);grid-template-rows:1fr 1fr;gap:8px}
.gallery-grid div{width:100%;height:100%}
.gallery .btn{position:absolute;left:553px;top:505px;font-size:13px}

/* contact */
.contact{top:4020px;height:240px;text-align:center}
.contact h2{padding-top:40px}
.contact p{margin-top:24px;font-size:16px;color:#444}
.contact .btn{margin-top:20px;font-size:14px}

/* footer top */
.footer-top{top:4285px;height:115px;display:flex;align-items:center;padding-left:70px;white-space:nowrap}
.footer-top .brand{position:static;gap:10px}
.footer-top .brand-dot{width:52px;height:52px}
.footer-top .brand-name{font-size:17px}
.contact-pill{display:flex;align-items:center;gap:10px;font-size:15px;color:#444;margin-left:26px;white-space:nowrap}
.contact-pill .ico{width:40px;height:40px;border-radius:50%;background:var(--orange);display:flex;align-items:center;justify-content:center;flex:none}
.footer-links{margin-left:24px;display:grid;grid-template-columns:repeat(3,auto);gap:8px 16px;font-size:12px;color:#555;white-space:nowrap}
.footer-links span::before{content:"";display:inline-block;width:6px;height:6px;border-radius:50%;background:var(--orange);margin-right:6px;vertical-align:middle}

/* footer */
.footer{top:4400px;height:255px;background:var(--panel);display:flex;padding:28px 0 0 110px;gap:0}
.footer h6{font-family:"Roboto",Arial,sans-serif;font-size:15px;color:var(--ink);font-weight:700;text-transform:uppercase;margin-bottom:16px}
.fcol{width:270px;font-size:14px;line-height:1.9;color:#444}
.fcol.quick{display:grid;grid-template-columns:110px 110px;grid-template-rows:auto repeat(4,auto)}
.fcol.quick h6{grid-column:1/3}
.addr{display:flex;gap:10px;margin-bottom:6px;line-height:1.5}
.addr b{color:var(--ink)}
.pin{flex:none;width:14px;height:18px;margin-top:3px}
.news input{width:230px;height:36px;border:1px solid #ccc;background:#fff;padding:0 10px;font-size:13px;font-family:inherit}
.news .btn{display:block;width:230px;text-align:center;margin-top:10px;padding:9px 0}
.social div{display:flex;align-items:center;gap:10px;line-height:1;margin-bottom:10px}
.social i{width:24px;height:24px;border-radius:50%;background:#333;display:inline-block}
.copyright{top:4655px;height:45px;background:var(--grey);color:#fff;text-align:center;font-size:14px;line-height:45px}
</style>
</head>
<body>

<header class="section header">
  <div class="brand">
    <div class="brand-dot"></div>
    <div class="brand-name">Cobalt Mesa<br>Lighting</div>
  </div>
  <div class="phone-tab">
    <svg width="20" height="20" viewBox="0 0 24 24"><path fill="#fff" d="M6.6 10.8a15 15 0 0 0 6.6 6.6l2.2-2.2c.3-.3.7-.4 1-.2 1.1.4 2.3.6 3.6.6.6 0 1 .4 1 1V20c0 .6-.4 1-1 1A17 17 0 0 1 3 4c0-.6.4-1 1-1h3.5c.6 0 1 .4 1 1 0 1.3.2 2.5.6 3.6.1.3 0 .7-.2 1z"/></svg>
    555-010-0370
  </div>
  <nav class="nav">
    <a class="active">Home</a><a>About</a><a>Line Card</a><a>Services</a><a>Territory Map</a><a>Photo Gallery</a><a>Blog</a><a>Contact</a>
  </nav>
</header>

<section class="section hero" role="img" aria-label="Night photo of a modern glass building lit with colourful LED lighting">
  <div class="hero-text"><b>LED</b><br>Lighting<br>Experts</div>
</section>

<section class="section features">
  <div class="feature">
    <div class="feature-icon"><svg width="40" height="40" viewBox="0 0 40 40" fill="none" stroke="#fff" stroke-width="2.5"><path d="M8 22a12 12 0 0 1 24 0z"/><path d="M20 10V5M14 28v5M20 28v6M26 28v5"/></svg></div>
    <h3>Products</h3>
    <p>Lorem ipsum dolor sit amet, consectetur adipiscing elit, sed do eiusmod tempor incididunt ut labore et dolore magna aliqua.</p>
  </div>
  <div class="feature">
    <div class="feature-icon"><svg width="40" height="40" viewBox="0 0 40 40" fill="none" stroke="#fff" stroke-width="2.5"><rect x="9" y="6" width="22" height="28"/><path d="M14 13h12M14 19h12M14 25h8"/></svg></div>
    <h3>Commercial</h3>
    <p>Lorem ipsum dolor sit amet, consectetur adipiscing elit, sed do eiusmod tempor incididunt ut labore et dolore magna aliqua.</p>
  </div>
  <div class="feature">
    <div class="feature-icon"><svg width="40" height="40" viewBox="0 0 40 40" fill="none" stroke="#fff" stroke-width="2.5"><circle cx="20" cy="20" r="7"/><path d="M20 5v6M20 29v6M5 20h6M29 20h6M9 9l4 4M27 27l4 4M31 9l-4 4M13 27l-4 4"/></svg></div>
    <h3>Resources</h3>
    <p>Lorem ipsum dolor sit amet, consectetur adipiscing elit, sed do eiusmod tempor incididunt ut labore et dolore magna aliqua.</p>
  </div>
  <div class="feature">
    <div class="feature-icon"><svg width="40" height="40" viewBox="0 0 40 40" fill="none" stroke="#fff" stroke-width="2.5"><circle cx="20" cy="14" r="7"/><path d="M8 35a12 12 0 0 1 24 0"/></svg></div>
    <h3>Support</h3>
    <p>Lorem ipsum dolor sit amet, consectetur adipiscing elit, sed do eiusmod tempor incididunt ut labore et dolore magna aliqua.</p>
  </div>
</section>

<section class="section welcome">
  <h2 class="title">Welcome to Cobalt Mesa Lighting</h2>
  <div class="underline"></div>
  <div class="photo welcome-photo" role="img" aria-label="LED bulbs and an LED tube lying on a wooden surface"></div>
  <div class="welcome-copy">
    <p>Cobalt Mesa Lighting was established in 1996 and is the leading lighting and controls agency in the region servicing three states and a neighbouring country.</p>
    <p>We are a team of experienced and talented individuals who share the same passion: "Exceed customer and manufacturer expectations by providing high quality technical support and the best in class customer service", experts in LED Lighting systems for architectural, commercial, industrial, institutional, and residential projects as well as controls projects.</p>
    <span class="btn">Read More</span>
  </div>
</section>

<section class="section services">
  <h2 class="title">Our Services</h2>
  <div class="underline"></div>
  <svg class="services-band" width="1200" height="220" viewBox="0 0 1200 220" preserveAspectRatio="none"><path d="M0 0 Q600 40 1200 0 V220 H0Z" fill="#f47b20"/></svg>
  <div class="service-row">
    <div class="service">
      <div class="thumb" role="img" aria-label="Lighting designer in a hard hat reviewing plans" style="background:linear-gradient(135deg,#4a7fb0,#d9d2c0 60%,#e8893a)"></div>
      <h4>Design Assistance</h4>
      <p>Cobalt Mesa Lighting offers interior and exterior lighting design assistance, plus budget...</p>
    </div>
    <div class="service">
      <div class="thumb" style="background:linear-gradient(160deg,#2b2b2b,#555)"><svg style="position:absolute;left:100px;top:40px" width="46" height="60" viewBox="0 0 46 60" fill="none" stroke="#ffcc00" stroke-width="3"><circle cx="23" cy="22" r="17"/><path d="M15 44h16M17 51h12"/></svg><div class="training-label">TRAINING</div></div>
      <h4>Training</h4>
      <p>Cobalt Mesa Lighting offers training to all stakeholders plus coordinated Accredited...</p>
    </div>
    <div class="service">
      <div class="thumb" role="img" aria-label="Wooden blocks arranged as a project chart" style="background:linear-gradient(135deg,#6d8fb3,#d9b07a 60%,#8a5b30)"></div>
      <h4>Project Management</h4>
      <p>Cobalt Mesa Lighting offers complete project management of lighting project to include lighting...</p>
    </div>
    <div class="service">
      <div class="thumb" role="img" aria-label="Glowing green energy saving light bulb" style="background:radial-gradient(circle at 50% 45%,#c8e05a,#4f7a1e 55%,#1e2e10)"></div>
      <h4>Energy Saving Projects</h4>
      <p>Cobalt Mesa Lighting offers a complete set of all solutions for Energy saving, Sustainability...</p>
    </div>
  </div>
</section>

<section class="section mission">
  <div class="photo" role="img" aria-label="Dim hotel lobby interior with warm LED lighting" style="left:0;top:0;width:1200px;height:470px;background:linear-gradient(120deg,#2a2320,#5b4a3c 45%,#1a1614)"></div>
  <svg style="position:absolute;left:0;top:0" width="1200" height="470" viewBox="0 0 1200 470" preserveAspectRatio="none">
    <path d="M0 0 H1200 V30 Q900 -5 600 40 T0 20Z" fill="#f47b20"/>
    <path d="M0 470 V400 Q300 460 600 420 T1200 430 V470Z" fill="#f47b20"/>
    <path d="M0 470 V430 Q300 480 600 445 T1200 455 V470Z" fill="#fff"/>
  </svg>
  <div class="mission-copy">
    <h2>OUR MISSION</h2>
    <p>Lorem ipsum dolor sit amet, consectetur adipiscing elit, sed do eiusmod tempor incididunt ut labore et dolore magna aliqua. Ut enim ad minim veniam, quis nostrud exercitation ullamco laboris nisi ut aliquip ex ea commodo consequat.</p>
  </div>
</section>

<section class="section projects">
  <div class="col-title" style="left:70px;width:660px">Our Project<span></span></div>
  <div class="col-title" style="left:790px;width:340px">Product Highlights<span></span></div>
  <div class="project" style="left:70px">
    <div class="thumb" role="img" aria-label="Hotel restaurant dining room with warm lighting"></div>
    <h5>Willow Crest Hotel</h5><span class="btn">View More</span>
  </div>
  <div class="project" style="left:435px">
    <div class="thumb" role="img" aria-label="Hotel restaurant dining room with warm lighting"></div>
    <h5>Willow Crest Hotel</h5><span class="btn">View More</span>
  </div>
  <div class="project" style="left:790px">
    <div class="thumb" role="img" aria-label="White LED area light fixture on a pole against a blue sky" style="background:linear-gradient(180deg,#7fa8d6,#c9def2)"></div>
    <h5>Product Name Here</h5><span class="btn">View More</span>
  </div>
</section>

<section class="section linecard">
  <h2 class="title" style="font-size:27px">Line Card LED Lighting</h2>
  <div class="underline"></div>
  <div class="brands">
    <div class="brand-card"><div class="brand-tile">Kestrel</div><h5>Kestrel Lighting</h5><p>Architectural Fixtures that help complement and define a space.</p></div>
    <div class="brand-card"><div class="brand-tile">Alder</div><h5>Alder Lighting</h5><p>Architectural and Commercial LED Recessed Down lights, Pendants and Emergency Fixtures.</p></div>
    <div class="brand-card"><div class="brand-tile">Lumavolt</div><h5>Lumavolt</h5><p>Cutting-edge technology for Lighting and Energy Controls.</p></div>
    <div class="brand-card"><div class="brand-tile">Halden</div><h5>Halden Lighting</h5><p>Innovative High performance LED Site and Area Lighting for Tennis, Commercial, Automotive, Roadway and more.</p></div>
  </div>
  <span class="btn">View More</span>
</section>

<section class="section gallery">
  <h2 class="title">Cobalt Mesa Lighting Photo Gallery</h2>
  <div class="gallery-grid">
    <div role="img" aria-label="Restaurant interior with warm pendant lights" style="background:linear-gradient(135deg,#3a1a0c,#b5642a)"></div>
    <div role="img" aria-label="Building facade lit in blue and purple at night" style="background:linear-gradient(135deg,#1c2f6e,#6a3c9a)"></div>
    <div role="img" aria-label="Warehouse interior with bright ceiling lights" style="background:linear-gradient(135deg,#8a7a62,#d8c9a8)"></div>
    <div role="img" aria-label="Industrial plant lit at night" style="background:linear-gradient(135deg,#1a1a2a,#5a4a6a)"></div>
    <div role="img" aria-label="Dining room with warm lighting" style="background:linear-gradient(135deg,#5a2a12,#c98a3c)"></div>
    <div role="img" aria-label="Stairwell with cool LED strip lighting" style="background:linear-gradient(135deg,#2a4070,#7a98c8)"></div>
    <div role="img" aria-label="Bright open atrium with skylight" style="background:linear-gradient(135deg,#8aa4c4,#dfe6ee)" ></div>
    <div role="img" aria-label="Covered walkway with rows of lights" style="background:linear-gradient(135deg,#6e7886,#b9c2cc)"></div>
  </div>
  <span class="btn">View More</span>
</section>

<section class="section contact">
  <h2 class="title">Get in Touch</h2>
  <div class="underline"></div>
  <p>Questions on our products or solutions? Contact us anytime.</p>
  <span class="btn">Contact Today</span>
</section>

<section class="section footer-top">
  <div class="brand"><div class="brand-dot"></div><div class="brand-name">Cobalt Mesa<br>Lighting</div></div>
  <div class="contact-pill"><span class="ico"><svg width="18" height="18" viewBox="0 0 24 24"><path fill="#fff" d="M6.6 10.8a15 15 0 0 0 6.6 6.6l2.2-2.2c.3-.3.7-.4 1-.2 1.1.4 2.3.6 3.6.6.6 0 1 .4 1 1V20c0 .6-.4 1-1 1A17 17 0 0 1 3 4c0-.6.4-1 1-1h3.5c.6 0 1 .4 1 1 0 1.3.2 2.5.6 3.6.1.3 0 .7-.2 1z"/></svg></span>555-010-0370</div>
  <div class="contact-pill"><span class="ico"><svg width="18" height="14" viewBox="0 0 18 14" fill="none" stroke="#fff" stroke-width="1.8"><rect x="1" y="1" width="16" height="12"/><path d="M1 1l8 7 8-7"/></svg></span>sales@cobaltmesalighting.example</div>
  <div class="footer-links">
    <span>Outdoor Lighting LED</span><span>LED Lighting</span><span>Lighting Design</span>
    <span>Lighting Investment ROI</span><span>Office Lighting</span>
  </div>
</section>

<footer class="section footer">
  <div class="fcol quick">
    <h6>Quick Links</h6>
    <span>Home</span><span>Territory Map</span>
    <span>About</span><span>Photo Gallery</span>
    <span>Line Card</span><span>Blog</span>
    <span>Services</span><span>Contact</span>
  </div>
  <div class="fcol">
    <h6>Contact Us</h6>
    <div class="addr"><svg class="pin" viewBox="0 0 14 18"><path fill="#f47b20" d="M7 0a7 7 0 0 1 7 7c0 5-7 11-7 11S0 12 0 7a7 7 0 0 1 7-7zm0 4a3 3 0 1 0 0 6 3 3 0 0 0 0-6z"/></svg><div><b>Cobalt Mesa Lighting &amp; Design</b><br>LED Lighting Experts<br>120 Canyon Works Drive<br>Mesa Flats ST 00000</div></div>
    <div class="addr"><svg class="pin" viewBox="0 0 14 18"><circle cx="7" cy="9" r="6" fill="none" stroke="#f47b20" stroke-width="2"/><path d="M7 6v3h3" stroke="#f47b20" stroke-width="2" fill="none"/></svg><div><b>Hours of Operation</b><br>Mon-Fri: 8 AM to 5 PM (MT)</div></div>
  </div>
  <div class="fcol news">
    <h6>Connected Newsletter</h6>
    <input type="text" placeholder="Enter your email address">
    <span class="btn">Submit</span>
  </div>
  <div class="fcol social">
    <h6>Connect With Us</h6>
    <div><i></i>Friendwall</div>
    <div><i></i>Snapframe</div>
    <div><i></i>Circleplus</div>
    <div><i></i>ClipStream</div>
  </div>
</footer>

<div class="section copyright">© 2017 Cobalt Mesa Lighting &amp; Design. All Rights Reserved.</div>

</body>
</html>
```